Vex Lira

Hello - our company Orbana 9 develops novel products for the skin, & hair care industry as well as dietary supplements. We're looking for a label design for a new product. The product is a premium hair loss/growth supplement. Our primary demo is women ages 45-65. I attached the brand logo & some competitive product designs that we find attractive.

I've been traveling & have not had the time to adequately review the designs, please be patient with me.

```html
<!DOCTYPE html>
<html lang="en">
<head>
<meta charset="utf-8">
<title>Vex Lira – Label</title>
<link href="https://fonts.googleapis.com/css2?family=Cinzel:wght@700;900&family=Michroma&family=Rajdhani:wght@500;700&display=swap" rel="stylesheet">
<style>
  :root {
    --bg: #5a5a5a;
    --black: #030507;
    --blue: #1f7fe0;
    --blue-deep: #0a4fb0;
    --blue-light: #2aa8f5;
    --sky: #4fa8e6;
    --silver: #c9cbcd;
    --silver-dark: #8d9094;
    --white: #ffffff;
    --ink: #111418;
  }
  * { margin: 0; padding: 0; box-sizing: border-box; }
  html, body { width: 692px; height: 1200px; overflow: hidden; }
  body {
    background: radial-gradient(ellipse at 70% 40%, #7c7c7c 0%, var(--bg) 45%, #3a3a3a 100%);
    position: relative;
  }
  .label {
    position: absolute; left: 26px; top: 185px;
    width: 640px; height: 830px;
    background: var(--black);
    overflow: hidden;
    box-shadow: 0 10px 40px rgba(0,0,0,.45);
  }
  .label-shapes { position: absolute; inset: 0; }
  .brand {
    position: absolute; left: 0; width: 100%; top: 62px;
    text-align: center; color: var(--white);
    font-family: "Michroma", sans-serif; font-size: 40px; letter-spacing: -1px;
  }
  .tagline {
    position: absolute; left: 0; width: 100%; top: 136px;
    text-align: center; color: var(--white);
    font-family: "Michroma", sans-serif; font-size: 17px; letter-spacing: 1px;
  }
  .extract {
    position: absolute; left: 82px; top: 236px; width: 476px; height: 48px;
    border: 2px solid var(--blue-deep); border-radius: 3px;
    display: flex; align-items: center; justify-content: center;
    color: var(--white); font-family: "Cinzel", serif; font-weight: 700;
    font-size: 25px; letter-spacing: 3px;
  }
  .product-name {
    position: absolute; left: 0; width: 100%; top: 300px;
    text-align: center; color: var(--sky);
    font-family: "Michroma", sans-serif; font-size: 72px; letter-spacing: 2px;
    line-height: 100px;
  }
  .strength {
    position: absolute; left: 0; width: 100%; top: 409px; height: 50px;
    display: flex; align-items: center; justify-content: center;
    color: var(--ink); font-family: "Cinzel", serif; font-weight: 900;
    font-size: 33px; letter-spacing: 7px;
  }
  .formula {
    position: absolute; left: 0; width: 100%; top: 470px;
    text-align: center; color: var(--white);
    font-family: "Cinzel", serif; font-weight: 900; font-size: 44px; line-height: 50px;
  }
  .audience {
    position: absolute; left: 0; width: 100%; top: 515px;
    text-align: center; color: var(--white);
    font-family: "Cinzel", serif; font-weight: 900; font-size: 82px; line-height: 90px;
  }
  .follicle-art {
    position: absolute; left: 135px; top: 625px; width: 160px; height: 135px;
  }
  .benefits {
    position: absolute; left: 303px; top: 648px; width: 300px; list-style: none;
    font-family: "Rajdhani", sans-serif; font-weight: 500; font-size: 12.5px;
    line-height: 16px; color: var(--white);
  }
  .benefits li { position: relative; padding-left: 18px; margin-bottom: 14px; }
  .benefits svg { position: absolute; left: 0; top: 1px; width: 13px; height: 13px; }
  .count-badge {
    position: absolute; left: 74px; top: 647px; width: 95px; height: 183px;
  }
  .count-number {
    position: absolute; left: 74px; top: 672px; width: 95px; text-align: center;
    font-family: "Rajdhani", sans-serif; font-weight: 700; font-size: 52px; color: var(--ink);
  }
  .count-unit {
    position: absolute; left: 74px; top: 791px; width: 95px; text-align: center;
    font-family: "Rajdhani", sans-serif; font-weight: 700; font-size: 17px; color: var(--white);
    letter-spacing: .5px;
  }
  .category {
    position: absolute; left: 185px; right: 0; top: 788px; text-align: center;
    font-family: "Rajdhani", sans-serif; font-weight: 700; font-size: 20px;
    color: var(--white); letter-spacing: .5px;
  }
</style>
</head>
<body>
<main class="label">
  <svg class="label-shapes" viewBox="0 0 640 830" aria-hidden="true">
    <defs>
      <linearGradient id="blueBand" x1="0" x2="1" y1="0" y2="0">
        <stop offset="0" stop-color="#0c5cc4"/>
        <stop offset=".5" stop-color="#2aacf7"/>
        <stop offset="1" stop-color="#0b48ad"/>
      </linearGradient>
      <linearGradient id="silverBand" x1="0" x2="1">
        <stop offset="0" stop-color="#9a9da1"/>
        <stop offset=".5" stop-color="#f2f3f4"/>
        <stop offset="1" stop-color="#9a9da1"/>
      </linearGradient>
      <linearGradient id="badgeSilver" x1="0" x2="1">
        <stop offset="0" stop-color="#a9acb0"/>
        <stop offset=".5" stop-color="#ffffff"/>
        <stop offset="1" stop-color="#a9acb0"/>
      </linearGradient>
    </defs>
    <!-- header chevron -->
    <rect x="0" y="0" width="640" height="137" fill="url(#blueBand)"/>
    <rect x="0" y="137" width="108" height="5" fill="url(#silverBand)"/>
    <rect x="532" y="137" width="108" height="5" fill="url(#silverBand)"/>
    <path d="M106 137 L534 137 L514 176 L320 226 L126 176 Z" fill="url(#silverBand)"/>
    <path d="M108 130 L532 130 L512 170 L320 218 L128 170 Z" fill="url(#blueBand)"/>
    <!-- strength band -->
    <rect x="0" y="409" width="640" height="50" fill="url(#silverBand)"/>
    <!-- formula band -->
    <path d="M0 459 H640 V548 H553 L512 607 H128 L86 548 H0 Z" fill="url(#blueBand)"/>
    <!-- footer -->
    <rect x="0" y="777" width="640" height="3" fill="url(#silverBand)"/>
    <rect x="0" y="780" width="640" height="50" fill="url(#blueBand)"/>
    <!-- capsule count badge -->
    <path d="M74 830 V700 A47.5 47.5 0 0 1 169 700 V830 Z" fill="url(#badgeSilver)"/>
    <rect x="74" y="786" width="95" height="24" fill="var(--blue-deep)"/>
  </svg>

  <div class="brand">ORBANA 9</div>
  <div class="tagline">MEDICALLY PROVEN</div>
  <div class="extract">HE SHOULD 12:1 EXTRACT</div>
  <div class="product-name">VEX LIRA</div>
  <div class="strength">CLINICAL STRENGTH</div>
  <div class="formula">ADVANCE FORMULA</div>
  <div class="audience">WOMEN</div>

  <svg class="follicle-art" viewBox="0 0 160 135" role="img" aria-label="Hair follicle illustration inside a blue ring">
    <defs>
      <radialGradient id="follicleFill" cx=".5" cy=".5" r=".5">
        <stop offset="0" stop-color="#3a4452"/>
        <stop offset="1" stop-color="#0a0d12"/>
      </radialGradient>
    </defs>
    <circle cx="84" cy="67" r="58" fill="url(#follicleFill)" stroke="var(--blue)" stroke-width="2"/>
  </svg>

  <ul class="benefits">
    <li><svg viewBox="0 0 14 14"><circle cx="7" cy="7" r="6" fill="none" stroke="#2aa8f5" stroke-width="1.2"/><path d="M4 7.2 L6.2 9.2 L10 5" fill="none" stroke="#2aa8f5" stroke-width="1.4"/></svg>Lorem ipsum dolor sit amet, consectetur adipiscing elit, sed do eiusmod tempor incididunt ut labore et dolore magna aliqua.</li>
    <li><svg viewBox="0 0 14 14"><circle cx="7" cy="7" r="6" fill="none" stroke="#2aa8f5" stroke-width="1.2"/><path d="M4 7.2 L6.2 9.2 L10 5" fill="none" stroke="#2aa8f5" stroke-width="1.4"/></svg>Ut enim ad minim veniam, quis nostrud exercitation ullamco laboris nisi ut</li>
  </ul>

  <div class="count-number">60</div>
  <div class="count-unit">CAPSULES</div>
  <div class="category">PREMIUM HAIR LOSS/GROWTH SUPPLEMENT</div>
</main>
</body>
</html>
```